Dental Business Card

I need Dental oriented business cards.
On the front side -
- on the first line, my name:
Dr Marlo Vintner
- on the second line (just underneath):
Doctor of Dental Medicine
- on the third line, or underneath that or in a corner, I would like the address and phone number:
5182 Ch. Birchfield
Montreal QC H2T 4B9
514-629-5074
- other than that i would maybe like a logo of a tooth, but i want it to be subtle and very basic!
- I would like the card to be preferably black or dark grey-ish with the writing in white
On the other side -
- 2-3 lines with the possibility to write the next appointment the box with the lines should be white, with the rest of the card being black

```html
<!DOCTYPE html>
<html lang="en">
<head>
<meta charset="UTF-8">
<title>Appointment Card – Back</title>
<style>
  :root {
    --card-black: #000000;
    --panel-white: #ffffff;
    --dot-ink: #111111;
  }
  html, body {
    margin: 0;
    padding: 0;
    width: 1200px;
    height: 686px;
    overflow: hidden;
    background: var(--card-black);
  }
  .card-back {
    position: relative;
    width: 1200px;
    height: 686px;
    background: var(--card-black);
  }
  .appointment-panel {
    position: absolute;
    left: 97px;
    top: 107px;
    width: 1007px;
    height: 471px;
    background: var(--panel-white);
  }
  .write-lines {
    position: absolute;
    left: 0;
    top: 0;
    width: 1007px;
    height: 471px;
  }
  .write-line {
    stroke: var(--dot-ink);
    stroke-width: 4;
    stroke-dasharray: 4 13.63;
  }
</style>
</head>
<body>
  <main class="card-back">
    <section class="appointment-panel" aria-label="Next appointment writing area">
      <svg class="write-lines" viewBox="0 0 1007 471" aria-hidden="true">
        <line class="write-line" x1="71" y1="135" x2="937" y2="135"/>
        <line class="write-line" x1="71" y1="278" x2="937" y2="278"/>
        <line class="write-line" x1="71" y1="421" x2="937" y2="421"/>
      </svg>
    </section>
  </main>
</body>
</html>
```